BHSC Business cards

We are an established dental practice that is looking for new business cards to match our new logo. We are looking for something unique and sophisticated.
BRIEF: Colours are black, silver and white. Include the company name, logo (including “Pelwick Heath Dental Care”) and phone number “03 9415 2876”.
Front - Include the company name, logo (including “Pelwick Heath Dental Care”) and phone number “03 9415 2876”.
Back - Include the company name,  “Pelwick Heath Dental Care”, phone number “03 9415 2876”. address "64A Tindle Street, Pelwick Heath, Vic 3187", "Email reception@pelwickheathdentalcare.com.au", the Dentist Name " Dr ................................"  Your next appointment "Day, date and time(am/pm)".  3 lines for 3 appointments please, and at the bottom "IF UNABLE TO KEEP THIS APPOINTMENT 48 HOURS NOTICE IS REQUIRED."
Try and be creative and different with the design, i've added an image for inspiration

Target Market(s)
ALL in need of dental
Industry/Entity Type
Dental Clinic
Look and feel
Each slider illustrates characteristics of the customer's brand and the style your logo design should communicate.

```html
<!DOCTYPE html>
<html lang="en">
<head>
<meta charset="utf-8">
<title>Pelwick Heath Dental Care – Business Cards</title>
<link rel="stylesheet" href="https://fonts.googleapis.com/css2?family=Montserrat:wght@400;500;600;700&display=swap">
<style>
  :root {
    --stage: #1c1c1d;
    --card-dark: #0b0b0c;
    --card-mid: #1a1a1b;
    --silver: #b9bbbe;
    --silver-light: #dcdde0;
    --white: #ffffff;
    --ink: #111112;
    --rule: #8a8c90;
  }
  * { box-sizing: border-box; margin: 0; padding: 0; }
  html, body { width: 800px; height: 1200px; overflow: hidden; }
  body {
    background: var(--stage);
    font-family: "Montserrat", sans-serif;
    color: var(--white);
    display: flex;
    flex-direction: column;
    align-items: center;
    justify-content: center;
    gap: 90px;
  }
  .card {
    width: 680px;
    height: 415px;
    background: linear-gradient(160deg, var(--card-mid), var(--card-dark) 60%);
    border-radius: 6px;
    box-shadow: 0 18px 40px rgba(0,0,0,.55);
    position: relative;
    overflow: hidden;
  }
  .icon { width: 14px; height: 14px; flex: none; fill: var(--silver); }

  /* Appointment side */
  .appointment { padding: 26px 34px; }
  .brand-header { display: flex; align-items: center; gap: 14px; }
  .brand-dot {
    width: 40px; height: 40px; border-radius: 50%;
    border: 2px solid var(--silver);
  }
  .brand-name {
    font-weight: 600; font-size: 24px; letter-spacing: 2px;
    color: var(--silver); line-height: 1;
  }
  .brand-sub {
    font-size: 11px; letter-spacing: 3px; color: var(--silver);
    margin-top: 5px;
  }
  .appt-tab {
    margin: 14px 0 0 150px;
    width: 330px;
    background: var(--silver-light);
    color: var(--ink);
    font-weight: 700; font-size: 13px; letter-spacing: 1.5px;
    text-align: center;
    padding: 6px 0;
    border-radius: 4px 4px 0 0;
  }
  .appt-panel {
    background: var(--white);
    color: var(--ink);
    border-radius: 8px;
    padding: 14px 20px 12px;
    font-size: 13px;
  }
  .appt-row { display: flex; align-items: flex-end; gap: 8px; height: 27px; }
  .appt-line { flex: 1; border-bottom: 1px solid var(--ink); height: 14px; }
  .appt-line.short { flex: 0 0 130px; }
  .contact-row {
    display: flex; gap: 22px; margin-top: 14px;
    font-size: 10.5px; color: var(--silver);
  }
  .contact-item { display: flex; align-items: center; gap: 6px; }
  .notice {
    display: flex; align-items: center; gap: 8px;
    margin-top: 12px; font-size: 11px; font-weight: 700;
    letter-spacing: .6px; color: var(--white);
  }
  .notice .icon { fill: var(--white); }

  /* Profile side */
  .profile { display: flex; align-items: center; padding: 0 40px; }
  .profile-brand {
    width: 250px; display: flex; flex-direction: column; align-items: center;
  }
  .profile-dot {
    width: 110px; height: 110px; border-radius: 50%; background: var(--white);
  }
  .profile-name {
    margin-top: 14px; text-align: center;
    font-weight: 600; font-size: 22px; letter-spacing: 1.5px;
    line-height: 1.2; color: var(--white);
  }
  .profile-divider { width: 1px; height: 230px; background: var(--rule); margin: 0 34px; }
  .profile-details { flex: 1; }
  .dentist-name { font-weight: 600; font-size: 18px; color: var(--white); }
  .dentist-role { font-size: 11px; color: var(--silver); margin: 3px 0 16px; }
  .detail { display: flex; align-items: center; gap: 8px; font-size: 11px; color: var(--silver); margin-bottom: 8px; }
</style>
</head>
<body>

<svg width="0" height="0" style="position:absolute">
  <defs>
    <symbol id="i-phone" viewBox="0 0 24 24"><path d="M6.6 10.8a15 15 0 0 0 6.6 6.6l2.2-2.2a1 1 0 0 1 1-.25 11.4 11.4 0 0 0 3.6.57 1 1 0 0 1 1 1V20a1 1 0 0 1-1 1A17 17 0 0 1 3 4a1 1 0 0 1 1-1h3.5a1 1 0 0 1 1 1c0 1.25.2 2.45.57 3.6a1 1 0 0 1-.25 1z"/></symbol>
    <symbol id="i-mail" viewBox="0 0 24 24"><path d="M3 5h18a1 1 0 0 1 1 1v12a1 1 0 0 1-1 1H3a1 1 0 0 1-1-1V6a1 1 0 0 1 1-1zm9 7 8-5H4z"/></symbol>
    <symbol id="i-pin" viewBox="0 0 24 24"><path d="M12 2a7 7 0 0 1 7 7c0 5-7 13-7 13S5 14 5 9a7 7 0 0 1 7-7zm0 4.5a2.5 2.5 0 1 0 0 5 2.5 2.5 0 0 0 0-5z"/></symbol>
    <symbol id="i-globe" viewBox="0 0 24 24"><path d="M12 2a10 10 0 1 0 0 20 10 10 0 0 0 0-20zm6.9 6h-3a15 15 0 0 0-1.4-3.9A8 8 0 0 1 18.9 8zM12 4c.8 1.1 1.5 2.5 1.9 4h-3.8c.4-1.5 1.1-2.9 1.9-4zM4.3 14a8 8 0 0 1 0-4h3.4a16 16 0 0 0 0 4zm.8 2h3a15 15 0 0 0 1.4 3.9A8 8 0 0 1 5.1 16zm3-8h-3a8 8 0 0 1 4.4-3.9A15 15 0 0 0 8.1 8zM12 20c-.8-1.1-1.5-2.5-1.9-4h3.8c-.4 1.5-1.1 2.9-1.9 4zm2.3-6H9.7a14 14 0 0 1 0-4h4.6a14 14 0 0 1 0 4zm.2 5.9a15 15 0 0 0 1.4-3.9h3a8 8 0 0 1-4.4 3.9zm1.8-5.9a16 16 0 0 0 0-4h3.4a8 8 0 0 1 0 4z"/></symbol>
    <symbol id="i-tick" viewBox="0 0 24 24"><path d="M9 16.2 4.8 12l-1.4 1.4L9 19 21 7l-1.4-1.4z"/></symbol>
  </defs>
</svg>

<section class="card appointment" aria-label="Appointment card">
  <header class="brand-header">
    <span class="brand-dot"></span>
    <div>
      <div class="brand-name">PELWICK HEATH</div>
      <div class="brand-sub">DENTAL CARE · 03 9415 2876</div>
    </div>
  </header>

  <div class="appt-tab">YOUR NEXT APPOINTMENT</div>
  <div class="appt-panel">
    <div class="appt-row"><span>Dr</span><span class="appt-line"></span></div>
    <div class="appt-row"><span>Date</span><span class="appt-line"></span><span>at</span><span class="appt-line short"></span><span>am / pm</span></div>
    <div class="appt-row"><span>Date</span><span class="appt-line"></span><span>at</span><span class="appt-line short"></span><span>am / pm</span></div>
    <div class="appt-row"><span>Date</span><span class="appt-line"></span><span>at</span><span class="appt-line short"></span><span>am / pm</span></div>
  </div>

  <div class="contact-row">
    <span class="contact-item"><svg class="icon"><use href="#i-mail"/></svg>reception@pelwickheathdentalcare.com.au</span>
    <span class="contact-item"><svg class="icon"><use href="#i-pin"/></svg>64A Tindle Street, Pelwick Heath, Vic 3187</span>
  </div>
  <p class="notice"><svg class="icon"><use href="#i-tick"/></svg>IF UNABLE TO KEEP THIS APPOINTMENT 48 HOURS NOTICE IS REQUIRED</p>
</section>

<section class="card profile" aria-label="Contact card">
  <div class="profile-brand">
    <span class="profile-dot"></span>
    <div class="profile-name">PELWICK HEATH<br>DENTAL CARE</div>
  </div>
  <span class="profile-divider"></span>
  <div class="profile-details">
    <div class="dentist-name">Dr. Pelwick Heath</div>
    <div class="dentist-role">General Dentist</div>
    <div class="detail"><svg class="icon"><use href="#i-phone"/></svg>03 9415 2876</div>
    <div class="detail"><svg class="icon"><use href="#i-globe"/></svg>www.pelwickheathdentalcare.com.au</div>
    <div class="detail"><svg class="icon"><use href="#i-mail"/></svg>reception@pelwickheathdentalcare.com.au</div>
    <div class="detail"><svg class="icon"><use href="#i-pin"/></svg>64A Tindle Street, Pelwick Heath, Vic 3187</div>
  </div>
</section>

</body>
</html>
```